One-Page Designed - Top 5 Tips for Curly Hair

I need a one-pager designed that looks friendly, informative, and natural, but that can be used as a PDF download for a website. the current website is not launched yet but the link is www.fernstudiodover.net for reference.

This piece will be the piece we send to clients once they log into our website and subscribe so it is a very important piece.

Fern Salon is an eco-friendly and holistically minded salon. Through research and education, we’ve curated a selection of less toxic hair color and hair styling products that offer professional results with the most natural ingredients on the market today. Whether you’re looking for a great haircut, expert grey coverage, bouncy curls or an amazing balayage, we’re here for you.

We’re dedicated to improving the locks of curly girls in the greater Boston area. We are curly hair experts who are committed to continuing education on the lasted curly hair cutting and coloring techniques. We’ll keep your curls healthy and fabulous with our carefully curated collection of products too.

Target Market(s)

Curly Hair Girls Who Want to Go to Natural Product Salon

Industry/Entity Type

Hair And Beauty

Font styles to use
Other font styles liked:
• Dancing Script and Arial Nova

Requirements
Must have
• Should have graphics that call out the tips and then have the blocks that go with them as the descriptions. Should be fun, friendly and informative. Final product should be send as a PDF.
• Colors should go with Hex: #5BC2E7 and Hex: #686A66 and Hex: #C8C9C7
• It should include their logo and a photo of the owner Marisol.
Nice to have
• Images that reflect the copy.

```html
<!DOCTYPE html>
<html lang="en">
<head>
<meta charset="utf-8">
<title>Top 5 Tips for Curly Hair – Fern Salon</title>
<link rel="stylesheet" href="https://fonts.googleapis.com/css2?family=Arimo:wght@400;700&family=Dancing+Script:wght@700&display=swap">
<style>
:root{
  --sky:#5BC2E7;
  --blue:#1f98d9;
  --blue-deep:#1b8bd0;
  --blue-band:#2a9fdc;
  --wave:#36aee6;
  --white:#ffffff;
  --grey:#686A66;
  --grey-light:#C8C9C7;
  --ink:#333333;
  --url:#2a8fc9;
}
*{margin:0;padding:0;box-sizing:border-box}
html,body{width:927px;height:1200px;overflow:hidden;background:var(--white)}
body{font-family:"Arimo",Arial,sans-serif;color:var(--white)}
.page{position:relative;width:927px;height:1200px}

.header{position:absolute;left:0;top:0;width:927px;height:260px;background:var(--blue-deep);overflow:hidden}
.header svg.waves{position:absolute;inset:0}
.title-top{position:absolute;left:119px;top:38px;font-size:42px;letter-spacing:1px;font-weight:400}
.title-script{position:absolute;left:66px;top:82px;font-family:"Dancing Script",cursive;font-size:118px;line-height:1;white-space:nowrap}
.divider{position:absolute;left:559px;top:52px;width:1px;height:163px;background:rgba(255,255,255,.7)}
.owner-name{position:absolute;left:590px;top:50px;font-size:23px;letter-spacing:1.5px}
.owner-photo{position:absolute;left:590px;top:92px;width:117px;height:117px;border:3px solid var(--white);background:linear-gradient(160deg,#e9e2da,#b48a70 55%,#2b2220)}
.owner-bio{position:absolute;left:725px;top:91px;width:148px;font-size:9px;line-height:14.2px}

.tips{position:absolute;left:0;top:260px;width:927px;height:806px;background:var(--blue)}
.portrait-bg{position:absolute;left:470px;top:150px;width:457px;height:656px;background:radial-gradient(ellipse at 55% 45%,rgba(120,210,240,.45),rgba(90,190,235,.15) 60%,rgba(0,0,0,0) 80%)}
.tip{position:absolute;left:0;width:927px}
.tip:nth-child(odd){background:rgba(255,255,255,.03)}
.tip-photo{position:absolute;left:88px;width:195px;height:130px;border:1px solid var(--white)}
.tip-num{position:absolute;left:60px;width:55px;height:55px;border-radius:50%;background:var(--white);color:var(--ink);font-size:34px;font-weight:700;display:flex;align-items:center;justify-content:center}
.tip-title{position:absolute;left:302px;font-size:21px;font-weight:700;letter-spacing:1.3px}
.tip-text{position:absolute;left:302px;width:556px;font-size:11.6px;line-height:18.5px}

.footer{position:absolute;left:0;top:1066px;width:927px;height:134px;background:var(--white);text-align:center}
.brand{margin-top:26px;font-size:48px;font-weight:700;color:var(--sky);letter-spacing:1px;line-height:1}
.url{margin-top:12px;font-size:13px;letter-spacing:3px;color:var(--url)}
</style>
</head>
<body>
<div class="page">
  <header class="header">
    <svg class="waves" width="927" height="260" viewBox="0 0 927 260">
      <path d="M0 180 C200 250 420 260 560 230 C700 200 800 120 927 70 L927 260 L0 260Z" fill="var(--blue)"/>
      <path d="M0 140 C180 200 380 210 540 160 C700 110 820 40 927 30 L927 0 L0 0Z" fill="var(--wave)" opacity=".35"/>
      <path d="M600 0 C720 40 820 60 927 80" stroke="rgba(255,255,255,.25)" stroke-width="3" fill="none"/>
    </svg>
    <div class="title-top">TOP 5 TIPS FOR</div>
    <div class="title-script">CurlyHair</div>
    <div class="divider"></div>
    <div class="owner-name">MARISOL VENTRELLA</div>
    <div class="owner-photo" role="img" aria-label="Portrait photo of salon owner Marisol"></div>
    <p class="owner-bio">Marisol is the owner of Fern Salon in Dover and Wellesley, MA. She is a Bloom advanced curly hair stylist and is certified in the Coil by Coil method. She is a curl advocate and a lover of natural and organic products.</p>
  </header>

  <main class="tips">
    <div class="portrait-bg" role="img" aria-label="Faint background photo of a woman with long curly hair"></div>

    <section class="tip" style="top:0;height:150px">
      <div class="tip-photo" style="top:10px;background:linear-gradient(120deg,#5a3b22,#b07a4a 50%,#3d2a1c)" role="img" aria-label="Photo of long curly brown hair"></div>
      <div class="tip-num" style="top:48px">1</div>
      <h2 class="tip-title" style="top:15px">CURL DIVERSITY</h2>
      <p class="tip-text" style="top:46px">Embrace the diversity of your curls. Yes, you will have “curl diversity” everyday and that’s okay. Being consistent with your haircare routine and avoiding the temptation to blow dry or straighten will do wonders for your hair over the long term. I promise, your overall curl or wave pattern will improve over time. I also promise that you will never have the same head of curls twice. Variety is the spice of life!</p>
    </section>

    <section class="tip" style="top:150px;height:166px">
      <div class="tip-photo" style="top:13px;background:linear-gradient(180deg,#bfe8f7,#6cc6ea 60%,#1f9ed3)" role="img" aria-label="Photo of clear cleanser bottles in splashing water"></div>
      <div class="tip-num" style="top:51px">2</div>
      <h2 class="tip-title" style="top:17px">KEEP CLEANSER GENTLE</h2>
      <p class="tip-text" style="top:49px">Keep your cleanser gentle and leave in a little bit of your conditioner. Using a cream based, no or low suds cleanser is the best way to insure you’re not stripping your hair of its natural oils. Once you’ve cleansed, condition and rinse very quickly, leaving a light amount of moisturizer in your hair. This provides a constant supply of the nourishment curls are always in need of. Apply your styling product right over your very wet, lightly conditioned curls and you’re all set.</p>
    </section>

    <section class="tip" style="top:316px;height:151px">
      <div class="tip-photo" style="top:12px;background:linear-gradient(90deg,#c8dfe3,#8aa8b3 50%,#2a2220)" role="img" aria-label="Photo of a smiling woman with curly hair wrapped in a scarf"></div>
      <div class="tip-num" style="top:50px">3</div>
      <h2 class="tip-title" style="top:15px">REST EASY</h2>
      <p class="tip-text" style="top:46px">Wrap your curls or waves in a silk scarf to avoid friction. If you’re rough sleeper and you wake up with your scarf wrapped somewhere between your neck and your armpit (me), a silk pillow case is a better and safer option. Less friction= smoother curls.</p>
    </section>

    <section class="tip" style="top:467px;height:174px">
      <div class="tip-photo" style="top:12px;left:85px;background:linear-gradient(130deg,#3a3a3a,#c9a57a 50%,#2c2c2c)" role="img" aria-label="Photo of a stylist trimming hair ends with scissors and comb"></div>
      <div class="tip-num" style="top:62px">4</div>
      <h2 class="tip-title" style="top:21px">KEEP YOUR ENDS BLUNT</h2>
      <p class="tip-text" style="top:52px">I’m not saying this because I’m a stylist, I swear. I’m saying this because I care about curly hair. Cutting curls every 6-10 weeks, depending on the length and curl type is essential to great hair health. Keeping your ends blunt and free of splits and frays will make styling easier and is especially important of you’re growing your hair longer. We all know how long that takes when you’re a curly girl.</p>
    </section>

    <section class="tip" style="top:641px;height:165px">
      <div class="tip-photo" style="top:17px;left:84px;background:radial-gradient(circle at 40% 60%,#f3eee2,#555 45%,#1e1e1e 75%,#ddd)" role="img" aria-label="Photo of a bowl of hair treatment cream with a brush"></div>
      <div class="tip-num" style="top:60px">5</div>
      <h2 class="tip-title" style="top:21px">AVOID SILICONES AND SULFATES</h2>
      <p class="tip-text" style="top:52px">You’ve heard this (pretty much everywhere) before but that’s only because it’s true. Silicones coat the hair and are extremely difficult to remove, leaving the hair with an altered texture and rendering it impervious to deep conditioning.  Use only reputable hair care products like those from Meadowleaf Organic Beauty or Ringlet Works. Beware of hidden silicones. They can be in the “fragrance” portion of the ingredient list.</p>
    </section>
  </main>

  <footer class="footer">
    <div class="brand">FERN SALON</div>
    <div class="url">www.fernstudiodover.net</div>
  </footer>
</div>
</body>
</html>
```